Professional & attention grabbing.

A business card design, front and back. I already have a logo I will attach, but I am open to something new as well.
Things to include:
Name:
Title:
Phone:
Email:
Wanting something that is professional but attention grabbing.
Also we do a lot of work using drones on natural gas pipelines (leading the future)if you want to include any of that. I'm open to ideas.
Target Market(s)
Natural gas transmission industry / greenhouse gas mitigation industry
Industry/Entity Type
Business
Contact Information for Business Card
All details have been conveyed above.
Colors
Designer to choose colors to be used in the design.
Look and feel
Each slider illustrates characteristics of the customer's brand and the style your logo design should communicate.

```html
<!DOCTYPE html>
<html lang="en">
<head>
<meta charset="UTF-8">
<title>Veltra Inspections – Business Card</title>
<link href="https://fonts.googleapis.com/css2?family=Roboto:wght@400;500;700&display=swap" rel="stylesheet">
<style>
  :root {
    --backdrop: #3b3431;
    --card: #161616;
    --card-edge: #202020;
    --brand-red: #c0232b;
    --logo-grey: #a7a9ab;
    --text-white: #f1f1f1;
    --text-muted: #8e8e8e;
    --divider: #5a5a5a;
  }
  * { margin: 0; padding: 0; box-sizing: border-box; }
  html, body {
    width: 1200px;
    height: 864px;
    overflow: hidden;
    background: var(--backdrop);
    font-family: "Roboto", Arial, sans-serif;
  }
  .canvas {
    width: 1200px;
    height: 864px;
    display: flex;
    align-items: center;
    justify-content: center;
    gap: 40px;
  }
  .card {
    width: 540px;
    height: 309px;
    background: var(--card);
    border: 1px solid var(--card-edge);
    box-shadow: 0 14px 30px rgba(0, 0, 0, 0.45);
    position: relative;
  }

  /* Front */
  .card-front {
    display: flex;
    flex-direction: column;
    align-items: center;
    justify-content: center;
    gap: 26px;
  }
  .brand-lockup {
    display: flex;
    align-items: center;
    gap: 16px;
  }
  .brand-mark {
    width: 44px;
    height: 44px;
    background: var(--brand-red);
  }
  .brand-name {
    color: var(--logo-grey);
    font-weight: 700;
    font-size: 40px;
    line-height: 1;
    letter-spacing: 0.5px;
  }
  .front-website {
    color: var(--text-muted);
    font-size: 14px;
    letter-spacing: 6px;
  }

  /* Back */
  .card-back {
    display: flex;
    align-items: center;
    padding-left: 70px;
  }
  .back-lockup {
    width: 150px;
    display: flex;
    flex-direction: column;
    align-items: flex-start;
    gap: 12px;
  }
  .back-lockup .brand-mark {
    width: 56px;
    height: 56px;
  }
  .back-lockup .brand-name {
    color: var(--text-white);
    font-size: 24px;
  }
  .divider {
    width: 1px;
    height: 130px;
    background: var(--divider);
    margin: 0 26px 0 12px;
  }
  .contact-name {
    color: var(--brand-red);
    font-size: 20px;
    font-weight: 500;
    line-height: 1.1;
  }
  .contact-title {
    color: var(--text-white);
    font-size: 16px;
    margin-bottom: 14px;
  }
  .contact-list { list-style: none; }
  .contact-list li {
    display: flex;
    align-items: center;
    gap: 10px;
    color: var(--text-white);
    font-size: 14px;
    line-height: 24px;
  }
  .contact-list svg {
    width: 13px;
    height: 13px;
    fill: var(--brand-red);
    flex: none;
  }
</style>
</head>
<body>
  <main class="canvas">
    <section class="card card-front" aria-label="Card front">
      <div class="brand-lockup">
        <span class="brand-mark"></span>
        <span class="brand-name">Veltra Inspections</span>
      </div>
      <p class="front-website">www.example.com</p>
    </section>

    <section class="card card-back" aria-label="Card back">
      <div class="back-lockup">
        <span class="brand-mark"></span>
        <span class="brand-name">Veltra</span>
      </div>
      <span class="divider"></span>
      <div class="contact">
        <p class="contact-name">Mark Ellery</p>
        <p class="contact-title">President</p>
        <ul class="contact-list">
          <li>
            <svg viewBox="0 0 16 16" aria-hidden="true"><path d="M3 1h3l1.5 4-2 1.3a9 9 0 0 0 4.2 4.2L11 8.5l4 1.5v3a2 2 0 0 1-2 2A13 13 0 0 1 1 3a2 2 0 0 1 2-2z"/></svg>
            555 0142 7788
          </li>
          <li>
            <svg viewBox="0 0 16 16" aria-hidden="true"><path d="M1 3h14v1.2L8 9 1 4.2z"/><path d="M1 5.6l7 4.8 7-4.8V13H1z"/></svg>
            mark@example.com
          </li>
          <li>
            <svg viewBox="0 0 16 16" aria-hidden="true"><circle cx="8" cy="8" r="7"/><path d="M1 8h14M8 1c-3 3.5-3 10.5 0 14M8 1c3 3.5 3 10.5 0 14" stroke="#161616" stroke-width="1.2" fill="none"/></svg>
            www.example.com
          </li>
        </ul>
      </div>
    </section>
  </main>
</body>
</html>
```